Flyer
Super tolle Arbeit, Greta hat sich wahnsinnige Mühe gegeben und ein perfektes Ergebnis geliefert. Jederzeit wieder!!!
Zielgruppe
Wir bauen hochwertige Design Esstische aus Holz auch Couchtische und Konferenztische unser Zielgruppe sind Menschen die Wert auch hochwertige Handarbeit legen und denen Design wichtig ist
Aufgabenstellung
Bitte designt einen Flyer, bei den Format bin ich offen, nur keine Spezial Formate die dann beim Drucken teurer sind. Ansonsten sollten Bilder unserer Tische zu sehen sein, außerdem ein Text mit der Beschreibung was wir machen, wofür wir stehen und was uns wichtig ist. Es sollte auch ein Bild von meinem Kollegen und mir zu sehen sein und die Kontaktdaten natürlich. Bilder und Texte könnt ihr der Website entnehmen. Wir stehen für ein minimalistisches und cleanes design und das sollte bei dem Flyer ebenfalls der Fall sein.

```html
<!DOCTYPE html>
<html lang="de">
<head>
<meta charset="utf-8">
<title>Felber Manufaktur – Faltflyer Innenseiten</title>
<link rel="stylesheet" href="https://fonts.googleapis.com/css2?family=Montserrat:wght@500;600&family=Nunito+Sans:wght@300;400;700&display=swap">
<style>
  :root {
    --backdrop: #9a9899;
    --paper: #fbfbfa;
    --paper-shade: #f1f0ef;
    --ink: #1d1d1d;
    --ink-soft: #555555;
    --wood-light: #e6d6c0;
    --wood-mid: #c9ad88;
    --wood-dark: #8a6c4b;
    --photo-dark: #3a3634;
    --photo-mid: #6b5d52;
  }
  * { box-sizing: border-box; margin: 0; padding: 0; }
  html, body {
    width: 1200px;
    height: 800px;
    overflow: hidden;
    background: var(--backdrop);
  }
  .spread {
    position: absolute;
    left: 60px;
    top: 130px;
    width: 1080px;
    height: 540px;
    display: flex;
    box-shadow: 0 18px 40px rgba(0,0,0,0.18);
  }
  .page {
    position: relative;
    width: 540px;
    height: 540px;
    background: var(--paper);
    overflow: hidden;
  }
  .page--left {
    background: linear-gradient(to right, var(--paper) 80%, var(--paper-shade));
    padding: 58px 60px 0 60px;
  }
  .headline {
    font-family: "Montserrat", sans-serif;
    font-weight: 600;
    font-size: 30px;
    line-height: 1.05;
    letter-spacing: 0.06em;
    color: var(--ink);
    text-transform: uppercase;
  }
  .subline {
    font-family: "Nunito Sans", sans-serif;
    font-weight: 300;
    font-size: 22px;
    line-height: 1.2;
    letter-spacing: 0.04em;
    color: var(--ink);
    margin-top: 8px;
  }
  .lead {
    font-family: "Nunito Sans", sans-serif;
    font-weight: 700;
    font-size: 12.5px;
    line-height: 1.6;
    color: var(--ink);
    margin-top: 18px;
    max-width: 330px;
  }
  .body-copy {
    font-family: "Nunito Sans", sans-serif;
    font-weight: 300;
    font-size: 12.5px;
    line-height: 1.6;
    color: var(--ink-soft);
    margin-top: 8px;
    max-width: 330px;
  }
  .board-edge {
    position: absolute;
    right: 0;
    top: 196px;
    width: 110px;
    height: 10px;
    background: linear-gradient(to right, var(--wood-mid), var(--wood-dark));
  }
  .page--right {
    background: linear-gradient(to left, var(--paper) 85%, var(--paper-shade));
  }
  .wood-field {
    position: absolute;
    left: 0; top: 0;
    width: 540px;
    height: 360px;
    background:
      radial-gradient(ellipse at 85% 70%, rgba(138,108,75,0.45), transparent 45%),
      radial-gradient(ellipse at 20% 20%, rgba(138,108,75,0.35), transparent 40%),
      linear-gradient(to bottom, var(--wood-mid) 0%, var(--wood-light) 60%, var(--paper) 100%);
  }
  .team-photo {
    position: absolute;
    left: 110px;
    top: 62px;
    width: 330px;
    height: 240px;
    background: linear-gradient(135deg, var(--photo-dark), var(--photo-mid) 60%, var(--wood-mid));
  }
  .founder-text {
    position: absolute;
    left: 80px;
    top: 372px;
    width: 390px;
    text-align: center;
    font-family: "Nunito Sans", sans-serif;
    font-size: 12.5px;
    line-height: 1.65;
    color: var(--ink-soft);
    font-weight: 300;
  }
  .founder-text strong { font-weight: 700; color: var(--ink); }
</style>
</head>
<body>
  <main class="spread">
    <section class="page page--left">
      <h1 class="headline">Zeitlose<br>Möbel<br>fürs Leben</h1>
      <p class="subline">Handgefertigt<br>für Generationen</p>
      <p class="lead">Wir möchten Möbel herstellen, die nicht nur von hoher Qualität sind, sondern auch ein Leben lang halten und zum Vererben geeignet sind.</p>
      <p class="body-copy">Unsere einzigartigen Unikate sollen Wohnräume bereichern und ein zeitloses Design verkörpern.</p>
      <p class="body-copy">Wir streben danach, vielen Menschen den Genuss unserer handgefertigten Möbel zu ermöglichen und dabei faire Arbeitsplätze zu schaffen.</p>
      <div class="board-edge" role="img" aria-label="Kante einer massiven Holzplatte"></div>
    </section>
    <section class="page page--right">
      <div class="wood-field" role="img" aria-label="Maserung einer Wurzelholz-Tischplatte"></div>
      <div class="team-photo" role="img" aria-label="Foto: die beiden Schreiner bei der Arbeit an einem Tisch in der Werkstatt"></div>
      <p class="founder-text"><strong>Ich bin Jonas Felber, Gründer der Felber Manufaktur.</strong><br>Schon als Kind lernte ich durch meinen Vater, einen Holzbildhauer, den Umgang mit Holz. Heute fertige ich gemeinsam mit Schreiner Lukas Brandt handgefertigte Unikate – von Esstischen aus monolithischen Bohlen bis zu Couchtischen, Waschtischplatten und Konferenztischen – direkt aus Stuttgart.</p>
    </section>
  </main>
</body>
</html>
```